Ridgeway Diesel web site banners

We are looking for a NEW banner design with a Halloween theme and just some new banners to use in general. If you go to our web site www.rwdiesel-example.com you will see our big banner that says "new product added daily" that's where it will go.

Please use our truck pictures below for the banner

Target Market(s)

Target the holiday themes

Industry/Entity Type

Diesel trucks

```html
<!DOCTYPE html>
<html lang="en">
<head>
<meta charset="utf-8">
<title>Ridgeway Diesel – New Product Added Daily</title>
<link rel="stylesheet" href="https://fonts.googleapis.com/css2?family=Creepster&family=Rubik:wght@700;800&display=swap">
<style>
  :root {
    --page: #ffffff;
    --night: #0b0c12;
    --moon-blue: #2a3aa8;
    --moon-glow: #b9b3e6;
    --amber: #fbb829;
    --amber-deep: #f39a12;
    --pumpkin: #ec8a3a;
    --pumpkin-deep: #c9561f;
    --truck: #2c2e34;
    --truck-deep: #16171b;
    --ink: #111111;
    --white: #ffffff;
  }
  * { margin: 0; padding: 0; box-sizing: border-box; }
  html, body { width: 1200px; height: 1000px; overflow: hidden; background: var(--page); }
  .canvas { position: relative; width: 1200px; height: 1000px; }
  .banner {
    position: absolute; left: 70px; top: 280px; width: 1060px; height: 423px;
    overflow: hidden; background: var(--night);
  }
  .night-sky {
    position: absolute; left: 0; top: 0; width: 560px; height: 310px;
    background:
      radial-gradient(circle at 140px 150px, var(--moon-glow) 0, #8d86d0 80px, transparent 170px),
      linear-gradient(115deg, var(--moon-blue) 0%, #1a1f5c 40%, var(--night) 80%);
  }
  .paint-splash {
    position: absolute; left: 460px; top: 0; width: 600px; height: 423px;
    background: linear-gradient(135deg, var(--amber) 0%, var(--amber-deep) 100%);
    clip-path: polygon(24% 0, 100% 0, 100% 100%, 14% 100%, 2% 84%, 13% 58%, 9% 32%);
  }
  .truck-photo {
    position: absolute; left: 605px; top: 14px; width: 450px; height: 400px;
    border-radius: 16px;
    background: linear-gradient(160deg, rgba(44,46,52,0.82) 0%, rgba(22,23,27,0.88) 70%, rgba(44,46,52,0.7) 100%);
  }
  .pumpkin {
    position: absolute; border-radius: 10px;
    background: linear-gradient(180deg, var(--pumpkin) 0%, var(--pumpkin-deep) 100%);
  }
  .pumpkin-top { left: 460px; top: 200px; width: 118px; height: 86px; }
  .pumpkin-front { left: 440px; top: 288px; width: 140px; height: 114px; }
  .pumpkin-corner { left: 2px; top: 330px; width: 86px; height: 82px; }
  .headline {
    position: absolute; font-family: "Creepster", cursive; font-weight: 400;
    color: var(--amber); letter-spacing: 1px; line-height: 1; white-space: nowrap;
    text-shadow: 3px 3px 0 var(--ink), -2px -2px 0 var(--ink), 2px -2px 0 var(--ink), -2px 2px 0 var(--ink), 6px 6px 0 var(--white);
  }
  .headline-top { left: 56px; top: 86px; font-size: 74px; }
  .headline-bottom { left: 100px; top: 186px; font-size: 68px; }
  .prompt-bar {
    position: absolute; left: 58px; top: 280px; width: 374px; height: 44px;
    background: #161616; transform: skewX(-14deg);
    border-bottom: 4px solid var(--amber-deep);
    display: flex; align-items: center; justify-content: center;
  }
  .prompt-bar span, .email-pill span {
    transform: skewX(14deg); font-family: "Rubik", sans-serif; font-weight: 800;
    white-space: nowrap;
  }
  .prompt-bar span { color: var(--white); font-size: 16.5px; }
  .email-pill {
    position: absolute; left: 102px; top: 340px; width: 290px; height: 33px;
    background: linear-gradient(90deg, var(--amber), var(--amber-deep));
    transform: skewX(-14deg);
    display: flex; align-items: center; justify-content: center;
  }
  .email-pill span { color: var(--ink); font-size: 14.5px; }
</style>
</head>
<body>
<div class="canvas">
  <section class="banner">
    <div class="night-sky" role="img" aria-label="Full moon behind bare tree branches in a blue night sky"></div>
    <div class="paint-splash" role="img" aria-label="Orange paint brush splash"></div>
    <div class="truck-photo" role="img" aria-label="Photo of a lifted black diesel pickup truck with open hood"></div>

    <h1 class="headline headline-top">NEW PRODUCT</h1>
    <h2 class="headline headline-bottom">ADDED DATIY</h2>

    <div class="prompt-bar"><span>DON'T SEE YOOUR ITEM? EMAIL US AT</span></div>
    <div class="email-pill"><span>SALES@RWDIESEL-EXAMPLE.COM</span></div>

    <div class="pumpkin pumpkin-top" role="img" aria-label="Jack-o'-lantern illustration"></div>
    <div class="pumpkin pumpkin-front" role="img" aria-label="Jack-o'-lantern illustration"></div>
    <div class="pumpkin pumpkin-corner" role="img" aria-label="Jack-o'-lantern illustration"></div>
  </section>
</div>
</body>
</html>
```